VelTrova an innovative way to connect sellers with car dealers

The idea is a site that connects consumers that want to sell thier cars with a dealer network that is ready to buy.

**I just added 9/26 a POSSIBLE logo. Dont feel obligated to use this or design off of it.

The first goal is to provide a place where people can SEAMLESSLY list their vechile for sale to a car dealership network. We are looking for people that want to get more for their car than trading it in allows but DONT want to go through the hassel of listing and selling their car on their own. The dont want to deal with people reaching out, showing the vechile, and the risk assocated with retailing a valuable item to the general public. That said these people dont want to just trade their car wholesale and buy retail. These are the people that that do to a place like AutoPlenz to sell their car directly. However AutoPlenz is just one dealer.

The second fuction of the site allows dealers to view the vechiles that have been listed especilaly the ones in thier market.

I would like to add that I am looking for real images. No cartoon or animation. Upmarket but friendly.

I have attached a detailed document to help.

Target Market(s)

People that want to sell cars and dealers that want to buy cars

Industry/Entity Type

Automotive

Requirements
Must have
• The pages listed in the document
Should not have
• No cartoon or animated images

```html
<!DOCTYPE html>
<html lang="en">
<head>
<meta charset="utf-8">
<title>VelTrova — Sell Your Car Hassle Free</title>
<link href="https://fonts.googleapis.com/css2?family=Outfit:wght@600;700;800&family=Urbanist:wght@400;500;600;700&display=swap" rel="stylesheet">
<style>
:root{
  --red:#d0181b;
  --red-dark:#8e0b0c;
  --ink:#111111;
  --text:#222222;
  --muted:#555555;
  --light:#f8f8f8;
  --white:#ffffff;
  --line:#d8d8d8;
  --hero-a:#1c2838;
  --hero-b:#3b4a5c;
}
*{box-sizing:border-box;margin:0;padding:0}
html,body{width:774px;height:1200px;overflow:hidden}
body{position:relative;background:var(--white);font-family:"Urbanist",sans-serif;color:var(--text)}
.abs{position:absolute}
/* top bar */
.topbar{left:0;top:0;width:774px;height:20px;background:var(--red)}
.social{display:flex;gap:7px;align-items:center}
.social span{width:9px;height:9px;border-radius:50%;background:var(--white);display:block}
.social span.active{border-radius:2px;background:#f04446;width:13px;height:13px}
.topbar .social{left:103px;top:4px}
.contact-top{top:4px;font-size:7px;font-weight:600;color:var(--white);display:flex;align-items:center;gap:4px}
/* hero */
.hero{left:0;top:0;width:774px;height:380px;background:linear-gradient(100deg,var(--hero-b) 0%,var(--hero-a) 55%,#0f1826 100%)}
.header{left:97px;top:20px;width:580px;height:40px;background:var(--white);border-radius:0 0 6px 6px}
.logo{font-family:"Outfit",sans-serif;font-weight:800;color:var(--ink);letter-spacing:.2px}
.header .logo{left:11px;top:8px;font-size:18px}
.nav{left:187px;top:11px;display:flex;align-items:center;font-size:6.3px;font-weight:600;color:#444;letter-spacing:.2px}
.nav a{color:inherit;text-decoration:none;padding:5px 8px}
.nav a.current{background:var(--red);color:var(--white);border-radius:2px}
.search{left:408px;top:11px;width:160px;height:18px;border:1px solid #e2e2e2;border-radius:3px;font-size:6px;color:#999;padding:5px 8px}
.search i{position:absolute;right:1px;top:1px;width:18px;height:14px;border-radius:3px;background:#444}
.hero-title{left:0;top:152px;width:774px;text-align:center;font-family:"Outfit",sans-serif;font-weight:800;font-size:31px;line-height:35px;color:var(--white)}
.hero-title em{font-style:normal;color:var(--red)}
.btn{font-size:7px;font-weight:600;text-align:center;text-decoration:none;display:block}
.btn-white{left:335px;top:238px;width:103px;height:22px;line-height:22px;background:var(--white);color:var(--ink);border-radius:2px}
.btn-red{background:var(--red);color:var(--white);border-radius:2px}
/* stats */
.stat{top:456px;width:150px;text-align:center}
.stat svg{display:block;margin:0 auto 6px}
.stat b{display:block;font-family:"Outfit",sans-serif;font-weight:800;font-size:18px;color:var(--red);line-height:20px}
.stat span{font-size:8px;color:var(--ink)}
/* testimonial */
.testi-bg{left:0;top:570px}
.stars{left:151px;top:636px;display:flex;gap:2px;align-items:center;font-size:7px;color:var(--red)}
.quote{left:152px;top:660px;width:350px;font-size:12px;line-height:15.3px;color:var(--ink);letter-spacing:.2px}
.rule{left:152px;top:753px;width:331px;height:1px;background:var(--line)}
.author{left:190px;top:766px}
.author b{display:block;font-size:8.5px;font-weight:700;color:var(--red)}
.author span{font-size:6.8px;color:var(--ink)}
.dots{left:109px;top:693px;display:flex;flex-direction:column;gap:6px}
.dots i{width:6px;height:6px;border:1px solid #f2bcbc;border-radius:50%;display:block}
.dots i.on{border-color:var(--red);background:radial-gradient(circle,var(--red) 35%,transparent 40%)}
.portrait{left:520px;top:644px;width:137px;height:137px;border-radius:50%;border:3px solid #f4dede;padding:3px}
.portrait div{width:100%;height:100%;border-radius:50%;background:linear-gradient(180deg,#e7e7e7 0%,#d7d2cc 55%,#6fa9c8 100%)}
/* cta */
.cta-title{left:168px;top:904px;width:300px;text-align:center;font-family:"Outfit",sans-serif;font-weight:800;font-size:18.5px;line-height:22px;color:var(--ink)}
.cta-btn{left:470px;top:918px;width:102px;height:22px;line-height:22px}
/* footer */
.footer-bg{left:0;top:970px}
.footer-logo{left:96px;top:1047px;font-size:18.5px;color:var(--white)}
.f-text{color:var(--white);font-size:6.2px;line-height:8.6px}
.f-head{font-family:"Outfit",sans-serif;font-weight:700;font-size:9.5px;color:var(--white)}
.f-list{list-style:none;color:var(--white);font-size:7px}
.f-list li{display:flex;gap:5px;align-items:flex-start}
.f-links li{margin-bottom:5.7px}
.f-links li:first-child{text-decoration:underline;opacity:.7}
.email-line{left:522px;top:1097px;width:153px;height:16px;border-bottom:1px solid rgba(255,255,255,.6);color:var(--white);font-size:6.8px;display:flex;align-items:center;gap:6px;padding-left:5px}
.submit{left:522px;top:1121px;width:62px;height:19px;line-height:19px;background:var(--white);color:var(--ink);border-radius:2px}
.bottom{left:0;top:1178px;width:774px;height:22px;background:var(--red-dark)}
.bottom p{position:absolute;left:98px;top:6px;font-size:7px;color:var(--white)}
.bottom .social{position:absolute;left:619px;top:5px}
</style>
</head>
<body>

<div class="hero abs" role="img" aria-label="Photo of a car dealer showing a client vehicle listings on a tablet"></div>
<svg class="abs" style="left:0;top:345px" width="774" height="65" viewBox="0 0 774 65">
  <polygon points="0,23 774,3 774,30 0,62" fill="var(--red-dark)"/>
  <polygon points="0,23 774,3 774,30 0,47" fill="var(--red)"/>
  <polygon points="0,62 774,30 774,65 0,65" fill="var(--white)"/>
</svg>

<div class="topbar abs"></div>
<div class="social abs" style="left:103px;top:5px"><span></span><span></span><span class="active" style="margin-top:-2px"></span><span></span></div>
<div class="contact-top abs" style="left:527px">
  <svg width="8" height="8" viewBox="0 0 24 24"><path d="M6.6 10.8a15 15 0 0 0 6.6 6.6l2.2-2.2a1 1 0 0 1 1-.25 11.4 11.4 0 0 0 3.6.57 1 1 0 0 1 1 1V20a1 1 0 0 1-1 1A17 17 0 0 1 3 4a1 1 0 0 1 1-1h3.5a1 1 0 0 1 1 1c0 1.25.2 2.45.57 3.6a1 1 0 0 1-.25 1z" fill="#fff"/></svg>555.210.4400</div>
<div class="contact-top abs" style="left:596px">
  <svg width="8" height="8" viewBox="0 0 24 24"><path d="M2 6h20v13H2z" fill="#fff"/><path d="M2 6l10 7 10-7" stroke="var(--red)" stroke-width="2" fill="none"/></svg>sales@veltrova.com</div>

<header class="header abs">
  <div class="logo abs">VELTROVA</div>
  <nav class="nav abs"><a class="current" href="#">HOME</a><a href="#">WHAT WE DO</a><a href="#">SIGN IN</a><a href="#">DEALERSHIP LOGIN</a></nav>
  <div class="search abs">Search by make, model, or keyword<i></i></div>
</header>

<h1 class="hero-title abs"><em>SELL</em> YOUR CAR<br>HASSLE <em>FREE</em></h1>
<a class="btn btn-white abs" href="#">SELL YOUR CAR NOW</a>

<!-- stats -->
<div class="stat abs" style="left:115px">
  <svg width="34" height="26" viewBox="0 0 34 26" fill="none" stroke="#111" stroke-width="1.3"><path d="M10 6l2-4h14l3 4v8"/><path d="M3 14l3-6h14l3 6v8H3z"/><rect x="8" y="17" width="10" height="3" fill="var(--red)" stroke="none"/><path d="M5 22v3M21 22v3"/></svg>
  <b>1856</b><span>Vehicle in stock cars</span></div>
<div class="stat abs" style="left:258px">
  <svg width="26" height="26" viewBox="0 0 26 26" fill="none" stroke="#111" stroke-width="1.3"><rect x="1" y="1" width="24" height="8" fill="var(--red)" stroke="none"/><circle cx="7" cy="15" r="2.5"/><circle cx="13" cy="13" r="2.5"/><circle cx="19" cy="15" r="2.5"/><path d="M2 25c0-4 2-6 5-6s5 2 5 6M8 22c0-4 2-6 5-6s5 2 5 6M14 25c0-4 2-6 5-6s5 2 5 6"/></svg>
  <b>1485</b><span>Satisfied customers</span></div>
<div class="stat abs" style="left:391px">
  <svg width="24" height="26" viewBox="0 0 24 26" fill="none" stroke="#111" stroke-width="1.3"><path d="M5 1h14v8a7 7 0 0 1-14 0z"/><path d="M5 4H1c0 4 2 6 4 6M19 4h4c0 4-2 6-4 6M12 16v4M7 24h10v-4H7z"/><circle cx="12" cy="8" r="3" fill="var(--red)" stroke="none"/></svg>
  <b>65+</b><span>Award achievement</span></div>
<div class="stat abs" style="left:517px">
  <svg width="30" height="24" viewBox="0 0 30 24" fill="none" stroke="#111" stroke-width="1.3"><path d="M2 23V1l27 8v14z"/><rect x="11" y="13" width="9" height="5" fill="var(--red)" stroke="none"/><path d="M1 23h28"/></svg>
  <b>10+</b><span>Total showroom</span></div>

<!-- testimonial -->
<svg class="testi-bg abs" width="774" height="300" viewBox="0 0 774 300"><polygon points="0,16 774,4 774,286 0,296" fill="var(--light)"/></svg>
<div class="stars abs">
  <svg width="60" height="9" viewBox="0 0 60 9"><g fill="var(--red)"><path id="st" d="M4.5 0l1.1 3h3.2L6.2 5l1 3.4-2.7-2-2.7 2 1-3.4L.2 3h3.2z"/><use href="#st" x="12"/><use href="#st" x="24"/><use href="#st" x="36"/><path d="M52.5 0l1.1 3h3.2L54.2 5l1 3.4-2.7-2z" /><path d="M52.5 0l-1.1 3h-3.2l2.6 2-1 3.4 2.7-2" fill="none" stroke="var(--red)" stroke-width=".8"/></g></svg>
  <span style="margin-left:4px">4.5</span></div>
<p class="quote abs">Lorem Ipsum is simply dummy text of the printing and typesetting industry. Lorem Ipsum has been the industry's standard dummy text ever since the 1500s, when an unknown printer took a galley of type and scrambled it to make a type specimen book.</p>
<div class="rule abs"></div>
<svg class="abs" style="left:151px;top:766px" width="31" height="24" viewBox="0 0 31 24" fill="none" stroke="var(--red)" stroke-width="1"><path d="M8 1C2 6 1 12 1 16a6 6 0 1 0 7-5"/><path d="M24 1c-6 5-7 11-7 15a6 6 0 1 0 7-5"/></svg>
<div class="author abs"><b>Daniel Moreau</b><span>Head of Data and AI at Roadmap Labs</span></div>
<div class="dots abs"><i></i><i></i><i class="on"></i><i></i></div>
<div class="portrait abs"><div role="img" aria-label="Portrait photo of the reviewer"></div></div>

<!-- cta -->
<h2 class="cta-title abs">DO YOU HAVE SOMETHING TO SELL THROUGH US?</h2>
<a class="btn btn-red cta-btn abs" href="#">SELL YOUR CAR NOW</a>

<!-- footer -->
<svg class="footer-bg abs" width="774" height="208" viewBox="0 0 774 208"><polygon points="0,50 774,8 774,208 0,208" fill="var(--red-dark)"/><polygon points="0,50 774,28 774,208 0,208" fill="var(--red)"/></svg>
<div class="logo footer-logo abs">VELTROVA</div>
<p class="f-text abs" style="left:96px;top:1086px;width:120px">Lorem Ipsum is simply dummy text of the printing and typesetting industry. Lorem Ipsum has been the industry's standard dummy text ever since the 1500s, when an unknown...</p>
<a class="f-text abs" style="left:96px;top:1137px;color:var(--red-dark);text-decoration:underline;font-weight:700">Readmore</a>

<h3 class="f-head abs" style="left:251px;top:1048px">Conatct info</h3>
<ul class="f-list abs" style="left:251px;top:1069px;width:140px">
  <li style="margin-bottom:6px"><svg width="8" height="10" viewBox="0 0 8 10"><path d="M4 0a4 4 0 0 1 4 4c0 3-4 6-4 6S0 7 0 4a4 4 0 0 1 4-4z" fill="var(--red-dark)"/><circle cx="4" cy="4" r="1.5" fill="var(--red)"/></svg><span style="line-height:12px">Lorem Ipsum, Riverton 00000<br>United States</span></li>
  <li style="margin-bottom:9px"><svg width="8" height="8" viewBox="0 0 24 24"><path d="M6.6 10.8a15 15 0 0 0 6.6 6.6l2.2-2.2a1 1 0 0 1 1-.25 11.4 11.4 0 0 0 3.6.57 1 1 0 0 1 1 1V20a1 1 0 0 1-1 1A17 17 0 0 1 3 4a1 1 0 0 1 1-1h3.5a1 1 0 0 1 1 1c0 1.25.2 2.45.57 3.6a1 1 0 0 1-.25 1z" fill="var(--red-dark)"/></svg>1-800-555-0142</li>
  <li style="margin-bottom:9px"><svg width="8" height="7" viewBox="0 0 8 7"><rect width="8" height="7" fill="var(--red-dark)"/><path d="M0 0l4 3.5L8 0" stroke="var(--red)" fill="none"/></svg>info@veltrova.com</li>
  <li><svg width="8" height="8" viewBox="0 0 8 8"><circle cx="4" cy="4" r="4" fill="var(--red-dark)"/></svg>Live location</li>
</ul>

<h3 class="f-head abs" style="left:410px;top:1048px">Quick Link</h3>
<ul class="f-list f-links abs" style="left:410px;top:1070px">
  <li>Home</li><li>What we do</li><li>Sign in</li><li>Dealership Login</li><li>Contact Us</li>
</ul>

<h3 class="f-head abs" style="left:522px;top:1048px">Stay In Touch</h3>
<p class="f-text abs" style="left:522px;top:1070px;width:120px;font-size:7px">Subscribe to our newsletter and stay updated</p>
<div class="email-line abs"><svg width="10" height="10" viewBox="0 0 10 10" fill="none" stroke="#fff" stroke-width=".9"><circle cx="5" cy="5" r="4.3"/><circle cx="5" cy="5" r="1.7"/></svg>Your email address*</div>
<a class="btn submit abs" href="#">SUBMIT</a>

<footer class="bottom abs">
  <p>© 2024 VelTrova. All Right Reserved</p>
  <div class="social"><span></span><span></span><span class="active" style="margin-top:-2px"></span><span></span></div>
</footer>

</body>
</html>
```